Business Cards and Stationery
Vellomar Development Company
I need single sided standard sized Business Card [3.5" x 2"]
Not sure. Use something compatible with logo.
Professional
Xxxx Xxxxxxx
President
12345 Xxxxxxxxx Xxxxx
Xxxxxxxxx, Xxxxxxxxxx 12345
xxxxxxxxxxx@xxxxxxxxx.xxx
Contractor's License No. 123456
Not that the information will serve as placeholders until the project is awarded and finalized. Actual information will be provided to create final source files.

```html
<!DOCTYPE html>
<html lang="en">
<head>
<meta charset="utf-8">
<title>Vellomar Development Company — Stationery</title>
<link rel="stylesheet" href="https://fonts.googleapis.com/css2?family=Open+Sans:wght@400;600;800&display=swap">
<style>
:root{
  --navy:#262b6b;
  --blue:#4a5299;
  --mist:#b7bbd4;
  --paper:#ffffff;
  --ink:#3a3c4a;
  --muted:#6d7080;
  --bg:#e4e5e9;
}
*{margin:0;padding:0;box-sizing:border-box}
html,body{width:1200px;height:840px;overflow:hidden;background:var(--bg);font-family:"Open Sans",Arial,sans-serif;color:var(--ink)}
.canvas{position:relative;width:1200px;height:840px}
.sheet{position:absolute;background:var(--paper);box-shadow:0 2px 8px rgba(0,0,0,.18);overflow:hidden}
.band{position:absolute;left:0;bottom:0;width:100%;background:linear-gradient(180deg,var(--mist) 0%,var(--blue) 45%,var(--navy) 100%)}
.brand{display:flex;align-items:center;gap:8px}
.brand-dot{border-radius:50%;background:var(--navy);flex:none}
.brand-name{font-weight:800;color:var(--navy);letter-spacing:.06em;text-transform:uppercase;line-height:1}

/* letterhead */
.letterhead{left:48px;top:44px;width:384px;height:760px;padding:26px 28px}
.letterhead .brand-dot{width:30px;height:30px}
.letterhead .brand-name{font-size:26px}
.letterhead .band{height:80px}
.letter-body{margin-top:38px;font-size:7.2px;line-height:1.5}
.letter-body p{margin-bottom:9px}
.letter-body .ref{font-size:6.6px;color:var(--muted);margin-top:-6px}
.signoff{margin-top:14px;font-size:7.2px;line-height:1.5}
.signature{width:58px;height:26px;margin:6px 0 2px;background:linear-gradient(90deg,#e7e8ef,#d3d5e2)}
.letter-footer{position:absolute;left:148px;bottom:104px;display:flex;gap:14px;font-size:6.2px;color:var(--muted);line-height:1.5}
.letter-footer .col{border-left:1px solid var(--mist);padding-left:6px}

/* envelope */
.envelope{left:540px;top:90px;width:612px;height:300px}
.envelope .brand{position:absolute;left:30px;top:26px}
.envelope .brand-dot{width:32px;height:32px}
.envelope .brand-name{font-size:28px}
.envelope .band{height:70px}
.envelope-address{position:absolute;right:34px;top:176px;font-size:8px;color:var(--muted)}
.envelope-address b{color:var(--navy);font-weight:600}

/* cards */
.card{width:264px;height:150px}
.card-front{left:590px;top:470px}
.card-back{left:880px;top:560px}
.card-holder{position:absolute;right:16px;top:14px;text-align:right;font-size:7px;line-height:1.45;color:var(--muted)}
.card-holder strong{display:block;font-size:8.5px;font-weight:600;color:var(--navy)}
.card-front .brand{position:absolute;left:18px;top:58px}
.card-front .brand-dot{width:22px;height:22px}
.card-front .brand-name{font-size:20px}
.card-front .band{height:44px}
.card-contact{position:absolute;left:18px;bottom:8px;display:flex;gap:16px;font-size:6.4px;line-height:1.5;color:#fff}
.card-back .brand{position:absolute;left:26px;top:36px}
.card-back .brand-dot{width:26px;height:26px}
.card-back .brand-name{font-size:22px}
.card-back .band{height:30px}
.card-web{position:absolute;right:18px;top:82px;font-size:8px;color:var(--navy);font-weight:600}
</style>
</head>
<body>
<main class="canvas">

  <section class="sheet letterhead">
    <div class="brand"><span class="brand-dot"></span><span class="brand-name">Vellomar</span></div>
    <div class="letter-body">
      <p>Dear,<br>Sir/Madam/Somebody</p>
      <p>We are pleased to confirm that the planning phase for the riverside residential project is now complete. Our team has reviewed the site surveys, coordinated with the city permit office and prepared a detailed schedule for the first phase of construction. Further documents will follow in the coming weeks, together with updated cost estimates and material specifications for your review.</p>
      <p class="ref">Section 1.2 of the project plan, revised in March</p>
      <p>Site preparation will begin once final approval has been received from all parties. During this period we ask that access to the property remain open to our crews and inspectors. Any questions regarding timelines, budget allocations or design changes may be directed to our project office, where a dedicated coordinator will respond within two business days of your request.</p>
      <p class="ref">Summary prepared by the site office</p>
      <p>We value the trust you have placed in our company and remain committed to delivering quality work on time and within budget. Our goal is a finished building that serves its owners and the community for many years to come. Thank you for choosing us as your development partner; we look forward to a long and productive working relationship.</p>
      <p class="ref">Section 3.1 of the project plan, revised in March</p>
    </div>
    <div class="signoff">
      Yours Truly,<br>On behalf of Vellomar
      <div class="signature" role="img" aria-label="Handwritten signature"></div>
      H. Marlowe
    </div>
    <div class="letter-footer">
      <div class="col">12345 Street Rd, Suite #<br>City State, Zip</div>
      <div class="col">(123) 456-7890<br>(123) 456-7891</div>
      <div class="col">info@vellomar.com<br>www.vellomar.com</div>
    </div>
    <div class="band" role="img" aria-label="Decorative navy and lavender footer band"></div>
  </section>

  <section class="sheet envelope">
    <div class="brand"><span class="brand-dot"></span><span class="brand-name">Vellomar</span></div>
    <div class="envelope-address">12345 Street Rd, Suite #, City State, Zip &nbsp;|&nbsp; <b>www.vellomar.com</b></div>
    <div class="band" role="img" aria-label="Decorative navy and lavender footer band"></div>
  </section>

  <section class="sheet card card-front">
    <div class="card-holder"><strong>Xxxx Xxxxxxx</strong>President<br>Contractor's License No. 123456</div>
    <div class="brand"><span class="brand-dot"></span><span class="brand-name">Vellomar</span></div>
    <div class="band" role="img" aria-label="Decorative navy and lavender footer band"></div>
    <div class="card-contact">
      <div>12345 Xxxxxxxxx Xxxxx<br>Xxxxxxxxx, Xxxxxxxxxx 12345</div>
      <div>(123) 456-7890<br>xxxxxxxxxxx@xxxxxxxxx.xxx</div>
    </div>
  </section>

  <section class="sheet card card-back">
    <div class="brand"><span class="brand-dot"></span><span class="brand-name">Vellomar</span></div>
    <div class="card-web">www.vellomar.com</div>
    <div class="band" role="img" aria-label="Decorative navy and lavender footer band"></div>
  </section>

</main>
</body>
</html>
```